flyer design for landscape group. i have enclosed my business card with logo

we are a local domestic and commercial landscaping group based in wokingham berkshire .we offer competitive landscaping solutions with a broad knowledge helping us solve problems in many fields such as new lawns, lawn care,tree care ,tree removal,hard and soft landscaping, decking, fencing ,garden or land clearance or just helping you with general maintanence. Being fully insured and certified for the job ,our excellent attention to detail has seen us recognised by local authorities and work for them on maintenance programmes performing in a safe and efficient manner

Target Market(s)

high end gardens commercial property

Industry/Entity Type

Landscaping

Requirements
Must have
• my logo . and some minimal sleek black and white design with small injections of colour
Should not have
• please do not include my full name or address only email and telephone

```html
<!DOCTYPE html>
<html lang="en">
<head>
<meta charset="utf-8">
<title>Greenfold Berkshire – Landscaping Flyer</title>
<link href="https://fonts.googleapis.com/css2?family=Montserrat:wght@300;400;500&family=Roboto:wght@400;700&display=swap" rel="stylesheet">
<style>
  :root{
    --stage:#e9e6e2;
    --paper:#f3f2f0;
    --panel-light:#dcdad7;
    --gravel:#2b2b2b;
    --path:#7a4e22;
    --brand-dark:#3a2418;
    --accent:#f39a1e;
    --ink:#2a1a12;
    --white:#ffffff;
  }
  *{margin:0;padding:0;box-sizing:border-box}
  html,body{width:1200px;height:1000px;overflow:hidden}
  body{background:var(--stage);position:relative;font-family:"Roboto",Arial,sans-serif}

  .flyer{position:absolute;overflow:hidden;background:var(--paper)}
  .flyer--front{left:52px;top:48px;width:526px;height:749px}
  .flyer--back{left:625px;top:217px;width:527px;height:747px}

  .front-scene{position:absolute;inset:0;
    background:linear-gradient(135deg,
      var(--panel-light) 0%, var(--panel-light) 31%,
      var(--gravel) 37%, var(--gravel) 52%,
      #3e3226 68%, var(--gravel) 84%, #2a3a2c 100%)}

  .brand{position:absolute;color:var(--brand-dark);font-family:"Montserrat",Arial,sans-serif;font-weight:300;text-align:center;line-height:1}
  .brand__name{display:block;font-size:30px;letter-spacing:1px;white-space:nowrap}
  .brand__region{display:block;font-size:13px;letter-spacing:4px;margin-top:10px}
  .brand__mark{display:block;width:14px;height:14px;background:var(--brand-dark);margin:0 auto 14px}
  .flyer--front .brand{left:12px;top:118px;width:210px}
  .flyer--back .brand{left:10px;top:120px;width:230px}

  .services{position:absolute;right:52px;top:139px;list-style:none;text-align:right;font-family:"Montserrat",Arial,sans-serif;font-weight:400;font-size:15px;color:var(--white);text-transform:uppercase}
  .services li{height:25px;display:flex;align-items:center;justify-content:flex-end;gap:8px;white-space:nowrap}
  .services svg{width:15px;height:15px;flex:none}

  .web-bar{position:absolute;left:100px;top:695px;width:426px;height:25px;background:var(--accent);color:var(--ink);font-family:"Roboto",Arial,sans-serif;font-weight:700;font-size:14px;text-align:right;padding-right:8px;line-height:25px}

  .tile{position:absolute}
  .tile--logo{left:0;top:0;width:250px;height:191px;background:var(--panel-light)}
  .tile--path{left:258px;top:0;width:269px;height:191px;background:linear-gradient(180deg,#b7a77a 0%,#8f8a5a 55%,#b4a37a 100%)}
  .tile--decking{left:0;top:199px;width:250px;height:217px;background:linear-gradient(160deg,#6a4a3a 0%,#8b8680 55%,#5f8f3a 100%)}
  .tile--lawn{left:258px;top:199px;width:269px;height:217px;background:linear-gradient(180deg,#6f7a5a 0%,#4e8a34 45%,#5cae3a 100%)}

  .about{position:absolute;left:0;top:416px;width:100%;height:280px;background:linear-gradient(180deg,#eef0ea 0%,#e6e9e2 100%);text-align:center;color:var(--ink);font-size:15.5px;line-height:20.5px;padding-top:32px}
  .about__lead{margin-bottom:10px}
  .about__rule{width:300px;height:1px;background:var(--accent);margin:0 auto 16px;opacity:.7}
  .about__pride{margin-top:14px;font-weight:700}
  .about strong{font-weight:700}

  .contact-bar{position:absolute;left:0;top:696px;width:100%;height:30px;background:var(--accent);color:var(--ink);font-size:13.5px;font-weight:700;display:flex;align-items:center;justify-content:center;gap:6px;white-space:nowrap}
  .contact-bar .sep{font-weight:400}
</style>
</head>
<body>

<section class="flyer flyer--front">
  <div class="front-scene" role="img" aria-label="Photo of a top-down garden scene: decking, dark chippings, a winding gravel path and round hedges"></div>

  <div class="brand">
    <span class="brand__mark"></span>
    <span class="brand__name">GREENFOLD</span>
    <span class="brand__region">BERKSHIRE</span>
  </div>

  <ul class="services">
    <li>New Lawns<svg viewBox="0 0 16 16"><circle cx="8" cy="8" r="8" fill="var(--accent)"/><path d="M4.5 8.3l2.4 2.3 4.6-4.8" fill="none" stroke="#fff" stroke-width="1.8"/></svg></li>
    <li>Lawn Treatments<svg viewBox="0 0 16 16"><circle cx="8" cy="8" r="8" fill="var(--accent)"/><path d="M4.5 8.3l2.4 2.3 4.6-4.8" fill="none" stroke="#fff" stroke-width="1.8"/></svg></li>
    <li>Tree Care<svg viewBox="0 0 16 16"><circle cx="8" cy="8" r="8" fill="var(--accent)"/><path d="M4.5 8.3l2.4 2.3 4.6-4.8" fill="none" stroke="#fff" stroke-width="1.8"/></svg></li>
    <li>Tree Removal<svg viewBox="0 0 16 16"><circle cx="8" cy="8" r="8" fill="var(--accent)"/><path d="M4.5 8.3l2.4 2.3 4.6-4.8" fill="none" stroke="#fff" stroke-width="1.8"/></svg></li>
    <li>Hard &amp; Soft Landscaping<svg viewBox="0 0 16 16"><circle cx="8" cy="8" r="8" fill="var(--accent)"/><path d="M4.5 8.3l2.4 2.3 4.6-4.8" fill="none" stroke="#fff" stroke-width="1.8"/></svg></li>
    <li>Decking<svg viewBox="0 0 16 16"><circle cx="8" cy="8" r="8" fill="var(--accent)"/><path d="M4.5 8.3l2.4 2.3 4.6-4.8" fill="none" stroke="#fff" stroke-width="1.8"/></svg></li>
    <li>Fencing<svg viewBox="0 0 16 16"><circle cx="8" cy="8" r="8" fill="var(--accent)"/><path d="M4.5 8.3l2.4 2.3 4.6-4.8" fill="none" stroke="#fff" stroke-width="1.8"/></svg></li>
    <li>Garden &amp; Land Clearance<svg viewBox="0 0 16 16"><circle cx="8" cy="8" r="8" fill="var(--accent)"/><path d="M4.5 8.3l2.4 2.3 4.6-4.8" fill="none" stroke="#fff" stroke-width="1.8"/></svg></li>
    <li>General Maintenance<svg viewBox="0 0 16 16"><circle cx="8" cy="8" r="8" fill="var(--accent)"/><path d="M4.5 8.3l2.4 2.3 4.6-4.8" fill="none" stroke="#fff" stroke-width="1.8"/></svg></li>
  </ul>

  <div class="web-bar">www.greenfoldlandscapes.co.uk</div>
</section>

<section class="flyer flyer--back">
  <div class="tile tile--logo">
    <div class="brand">
      <span class="brand__name">GREENFOLD</span>
      <span class="brand__region">BERKSHIRE</span>
    </div>
  </div>
  <div class="tile tile--path" role="img" aria-label="Photo of a paved front path with clipped topiary trees by a stone house"></div>
  <div class="tile tile--decking" role="img" aria-label="Photo of curved decking edged with gravel and a leafy shrub"></div>
  <div class="tile tile--lawn" role="img" aria-label="Photo of a fresh lawn beside a curving block-paved path and stone steps"></div>

  <div class="about">
    <p class="about__lead">We are a landscaping group based in Wokingham, Berkshire.</p>
    <div class="about__rule"></div>
    <p>We currently work for <strong>domestic and commercial</strong> clients<br>
    including local authorities. We offer <strong>competitive landscaping<br>
    solutions</strong> to suit every client, from garden and land clearance<br>
    to tree removal and decking.<br>
    We are also experienced groundworkers and undertake<br>
    <strong>all aspects of hard and soft landscaping.</strong></p>
    <p class="about__pride">We pride ourselves on carrying out high quality,<br>
    safe and efficient work paying excellent attention to detail.</p>
  </div>

  <div class="contact-bar">
    <span>www.greenfoldlandscapes.co.uk</span><span class="sep">|</span>
    <span>info@greenfoldlandscapes.co.uk</span><span class="sep">|</span>
    <span>07700900123</span>
  </div>
</section>

</body>
</html>
```